Business Cards

I'd like help creating business cards with the full logo "Veltrona Capital Partners" on the back of the card (navy background with white writing), and abbreviated logo "VCP" on the front. Would like to list name, title, phone number, email, and website listed on front of card. Would like to keep very simple. Front font Arial or similar.

```html
<!DOCTYPE html>
<html lang="en">
<head>
<meta charset="utf-8">
<title>Veltrona Capital Partners — Business Cards</title>
<link rel="stylesheet" href="https://fonts.googleapis.com/css2?family=Arimo:wght@400;700&family=Montserrat:wght@700&display=swap">
<style>
  :root {
    --navy: #1f3768;
    --ink: #1c1c1c;
    --paper: #ffffff;
    --backdrop: #a2a6a7;
  }
  * { margin: 0; padding: 0; box-sizing: border-box; }
  html, body { width: 1179px; height: 1200px; overflow: hidden; }
  body {
    background: var(--backdrop);
    position: relative;
    font-family: "Arimo", Arial, sans-serif;
    color: var(--ink);
  }
  .card {
    position: absolute;
    left: 219px;
    width: 742px;
    height: 423px;
    background: var(--paper);
  }
  .card--back { top: 161px; background: var(--navy); }
  .card--front { top: 617px; }

  .wordmark {
    position: absolute;
    font-family: "Montserrat", Arial, sans-serif;
    font-weight: 700;
    color: var(--navy);
    text-align: center;
    line-height: 1;
  }
  .wordmark__name { display: block; }
  .wordmark__tag { display: block; }

  .card--back .wordmark {
    left: 40px; width: 662px; top: 140px;
    color: var(--paper);
  }
  .card--back .wordmark__name { font-size: 100px; letter-spacing: 1px; }
  .card--back .wordmark__tag {
    font-size: 34px; letter-spacing: 14px; margin-top: 20px; margin-right: -14px;
  }

  .card--front .wordmark {
    left: 316px; width: 402px; top: 290px;
  }
  .card--front .wordmark__name { font-size: 62px; letter-spacing: 1px; }
  .card--front .wordmark__tag {
    font-size: 21px; letter-spacing: 8px; margin-top: 14px; margin-right: -8px;
  }

  .monogram {
    position: absolute;
    left: 60px; top: 44px;
    font-family: "Montserrat", Arial, sans-serif;
    font-weight: 700;
    font-size: 128px;
    line-height: 1;
    color: var(--navy);
    letter-spacing: -2px;
  }

  .person {
    position: absolute;
    right: 28px; top: 26px;
    text-align: right;
  }
  .person__name {
    font-weight: 700; font-size: 29px; color: var(--navy); line-height: 1.1;
  }
  .person__title { font-size: 20px; margin-top: 3px; }
  .accent-bar {
    position: absolute;
    right: 0; top: 27px;
    width: 16px; height: 53px;
    background: var(--navy);
  }

  .contact {
    position: absolute;
    left: 29px; top: 247px;
    font-size: 20px;
    line-height: 28px;
    color: #2a2a2a;
  }
  .contact__address { margin-bottom: 14px; }
  .contact__row { display: flex; align-items: center; gap: 6px; }
  .contact__row svg { width: 18px; height: 18px; flex: none; fill: var(--navy); }
</style>
</head>
<body>

  <section class="card card--back" aria-label="Card back">
    <div class="wordmark">
      <span class="wordmark__name">VELTRONA</span>
      <span class="wordmark__tag">CAPITAL PARTNERS</span>
    </div>
  </section>

  <section class="card card--front" aria-label="Card front">
    <div class="monogram">VCP</div>

    <div class="person">
      <div class="person__name">DANIEL MARSH</div>
      <div class="person__title">Managing Director</div>
    </div>
    <div class="accent-bar"></div>

    <div class="contact">
      <div class="contact__address">Your address, City<br>State, Zip 1234</div>
      <div class="contact__row">
        <svg viewBox="0 0 24 24" aria-hidden="true"><path d="M6.6 10.8a15.1 15.1 0 0 0 6.6 6.6l2.2-2.2c.3-.3.7-.4 1-.2 1.1.4 2.3.6 3.6.6.6 0 1 .4 1 1V20c0 .6-.4 1-1 1A17 17 0 0 1 3 4c0-.6.4-1 1-1h3.5c.6 0 1 .4 1 1 0 1.300.2 2.5.6 3.6.1.3 0 .7-.2 1z"/></svg>
        <span>123 456 789</span>
      </div>
      <div class="contact__row">
        <svg viewBox="0 0 24 24" aria-hidden="true"><path d="M2 6h20v13H2zm2 2v.4l8 5.2 8-5.2V8l-8 5z"/></svg>
        <span>info@yourmail.com</span>
      </div>
      <div class="contact__row">
        <svg viewBox="0 0 24 24" aria-hidden="true"><path d="M12 2a10 10 0 1 0 0 20 10 10 0 0 0 0-20zm-1 17.9A8 8 0 0 1 4.2 10l4.8 4.8V16a2 2 0 0 0 2 2zm6.9-2.5A2 2 0 0 0 16 16h-1v-3a1 1 0 0 0-1-1H8v-2h2a1 1 0 0 0 1-1V7h2a2 2 0 0 0 2-2v-.4a8 8 0 0 1 2.9 12.8z"/></svg>
        <span>www.yourwebsite.com</span>
      </div>
    </div>

    <div class="wordmark">
      <span class="wordmark__name">VELTRONA</span>
      <span class="wordmark__tag">CAPITAL PARTNERS</span>
    </div>
  </section>

</body>
</html>
```